Velmora Brightstead Website

Create website for Legal Management Company which specializes in Law Office Spersriinal Management
System implementation & Training
Global presence
Paralegal Services - Remote or In-Office
Legal Research
- Judge Motion Ruling History
- Opposing Counsel Opposition Research - Historical Filings - Pattern identification
Service by Mail - Ex- Parte Notice

Probate -Heir Finder - Asset Location -

```html
<!DOCTYPE html>
<html lang="en">
<head>
<meta charset="utf-8">
<title>Velmora Brightstead — Legal Ops Management</title>
<link href="https://fonts.googleapis.com/css2?family=Oswald:wght@300;400;500;600&family=EB+Garamond:ital,wght@0,400;1,400&family=IBM+Plex+Mono:wght@400&display=swap" rel="stylesheet">
<style>
:root{
  --ink:#111111;
  --ink-soft:#1b1c20;
  --paper:#f4f4f4;
  --white:#ffffff;
  --accent:#b5541c;
  --muted:#6b6b6b;
  --line:#e2e2e2;
  --line-dark:#2c2d33;
  --display:'Oswald',sans-serif;
  --serif:'EB Garamond',serif;
  --mono:'IBM Plex Mono',monospace;
}
*{box-sizing:border-box;margin:0;padding:0}
html,body{width:1200px;height:2695px;overflow:hidden}
body{position:relative;background:var(--paper);font-family:var(--serif);color:var(--ink)}
.sidebar{position:absolute;left:0;top:0;width:162px;height:2695px;background:var(--ink);color:#cfcfcf}
.brand{position:absolute;left:16px;top:16px;font-family:var(--display);font-weight:500;font-size:17px;line-height:1.05;color:var(--white);text-transform:uppercase;width:130px}
.brand::after{content:"";display:block;width:32px;height:3px;background:var(--accent);margin-top:10px}
.nav{position:absolute;left:16px;top:372px;list-style:none}
.nav li{font-style:italic;font-size:12px;color:#bdbdbd;margin-bottom:17px}
.side-foot{position:absolute;left:16px;bottom:16px;font-family:var(--display);font-size:8px;letter-spacing:1px;color:#9a9a9a;line-height:2}
.eyebrow{font-family:var(--display);font-weight:500;font-size:9px;letter-spacing:1.4px;color:var(--accent);text-transform:uppercase}
.hero{position:absolute;left:162px;top:0;width:1038px;height:808px}
.hero-text{position:absolute;left:0;top:0;width:608px;height:808px;
  background-color:var(--paper);
  background-image:linear-gradient(#e9e9e9 1px,transparent 1px),linear-gradient(90deg,#e9e9e9 1px,transparent 1px);
  background-size:24px 24px}
.hero-copy{position:absolute;left:63px;top:240px}
.hero-title{font-family:var(--display);font-weight:500;font-size:72px;line-height:63px;margin-top:10px;text-transform:uppercase}
.hero-title .dot{color:var(--accent)}
.hero-lede{font-size:16px;line-height:21px;color:#444;width:340px;margin-top:16px}
.cta{display:inline-flex;align-items:center;gap:8px;margin-top:24px;font-family:var(--display);font-size:9px;letter-spacing:1.2px;font-weight:500;padding-bottom:3px;border-bottom:1.5px solid var(--ink)}
.hero-photo{position:absolute;left:608px;top:0;width:430px;height:808px;background:linear-gradient(160deg,#c9c9c9 0%,#7a7a7a 35%,#2b2b2b 70%,#151515 100%)}
.status{position:absolute;left:21px;top:728px;width:392px;height:62px;background:var(--white);border-left:3px solid var(--accent);padding:16px 16px 0 16px}
.status-label{font-family:var(--display);font-size:7.5px;letter-spacing:1px;color:#555}
.status-text{font-style:italic;font-size:11.5px;margin-top:4px}
.status svg{position:absolute;right:16px;top:30px}
.services{position:absolute;left:162px;top:808px;width:1038px;height:813px}
.services-intro{position:absolute;left:40px;top:297px;width:270px}
.section-title{font-family:var(--display);font-weight:400;font-size:32px;line-height:33px;text-transform:uppercase;margin-top:8px}
.services-intro p{font-size:11px;line-height:18px;color:#444;margin-top:22px}
.stats{display:flex;margin-top:22px}
.stat{font-family:var(--display);text-align:center;padding:0 10px}
.stat:first-child{padding-left:0;border-right:1px solid #ccc}
.stat b{display:block;font-weight:500;font-size:19px}
.stat span{font-size:7px;letter-spacing:.5px;color:#555}
.service-list{position:absolute;left:346px;top:0;width:692px;height:813px;background:var(--white);border-left:1px solid var(--line)}
.service{height:102px;border-bottom:1px solid var(--line);display:flex;padding:30px 36px 0 31px}
.service-name{width:337px}
.service-name h3{font-family:var(--display);font-weight:400;font-size:16px;text-transform:uppercase}
.service-name em{font-size:9px;color:#777;display:block;margin-top:4px}
.service p{font-size:9px;line-height:15px;color:#555;width:288px;margin-top:2px}
.research{position:absolute;left:162px;top:1621px;width:1038px;height:472px;background:var(--ink);color:var(--white)}
.research-head{position:absolute;left:145px;top:64px;width:751px;height:116px;border-bottom:1px solid var(--line-dark)}
.research-head .section-title{font-size:33px;line-height:34px;margin-top:6px}
.research-quote{position:absolute;right:0;top:54px;width:200px;text-align:right;font-style:italic;font-size:10px;line-height:15px;color:#9a9a9a}
.cards{position:absolute;left:145px;top:201px;display:flex;gap:31px}
.card{width:360px;height:208px;background:var(--ink-soft);border:1px solid var(--line-dark);padding:20px 21px;position:relative}
.tag{position:absolute;right:21px;top:22px;font-family:var(--display);font-size:7px;letter-spacing:.5px;border:1px solid #888;padding:2px 5px}
.card h4{font-family:var(--display);font-weight:400;font-size:15px;margin-top:14px}
.card p{font-size:9.5px;line-height:17px;color:#aaa;margin-top:10px}
.card ul{list-style:none;margin-top:12px}
.card li{font-family:var(--mono);font-size:9px;color:#999;line-height:18px}
.card li::before{content:"";display:inline-block;width:5px;height:5px;border-radius:50%;background:var(--accent);margin-right:6px;vertical-align:1px}
.contact{position:absolute;left:162px;top:2093px;width:1038px;height:602px}
.contact-title{position:absolute;left:0;width:1038px;top:104px;text-align:center;font-family:var(--display);font-size:31px;text-transform:uppercase}
.contact-title::after{content:"";display:block;width:62px;height:3px;background:var(--accent);margin:10px auto 0}
.form{position:absolute;left:302px;top:197px;width:437px;height:279px;background:var(--white);border-top:3px solid var(--accent);box-shadow:0 12px 30px rgba(0,0,0,.06);padding:26px 31px}
.field{font-family:var(--display);font-size:9.5px;letter-spacing:1px;color:#999;border-bottom:1px solid #ddd;padding-bottom:6px}
.row{display:flex;gap:21px}
.row .field{flex:1}
.select{margin-top:30px;color:var(--ink);letter-spacing:0;display:flex;justify-content:space-between}
.details{margin-top:36px;height:56px}
.submit{margin-top:24px;height:36px;background:var(--ink);color:var(--white);font-family:var(--display);font-size:10px;letter-spacing:1.2px;display:flex;align-items:center;justify-content:center;gap:8px}
.legal{position:absolute;left:0;width:1038px;top:514px;text-align:center;font-style:italic;font-size:9px;line-height:13px;color:#777}
</style>
</head>
<body>
<aside class="sidebar">
  <div class="brand">Velmora Brightstead</div>
  <ul class="nav">
    <li>Overview</li><li>Expertise &amp; Ops</li><li>Intelligence</li><li>Contact</li>
  </ul>
  <div class="side-foot">NEW YORK • LONDON • TOKYO<br>© 2024</div>
</aside>

<section class="hero">
  <div class="hero-text">
    <div class="hero-copy">
      <div class="eyebrow">System Implementation &amp; Training</div>
      <h1 class="hero-title">Legal<br>Ops<span class="dot">.</span><br>Mgmt</h1>
      <p class="hero-lede">We build the infrastructure for modern law firms. From global paralegal staffing to high-fidelity opposition research.</p>
      <div class="cta">INITIATE INQUIRY
        <svg width="10" height="8" viewBox="0 0 10 8"><path d="M0 4h9M6 1l3 3-3 3" fill="none" stroke="#111" stroke-width="1.2"/></svg>
      </div>
    </div>
  </div>
  <div class="hero-photo" role="img" aria-label="Black and white photo looking up at glass office towers">
    <div class="status">
      <div class="status-label">CURRENT STATUS</div>
      <div class="status-text">Accepting new probate &amp; complex litigation clients.</div>
      <svg width="14" height="14" viewBox="0 0 14 14" fill="none" stroke="#b5541c" stroke-width="1.1"><circle cx="7" cy="7" r="6"/><ellipse cx="7" cy="7" rx="2.6" ry="6"/><path d="M1 7h12"/></svg>
    </div>
  </div>
</section>

<section class="services">
  <div class="services-intro">
    <div class="eyebrow">Core Competencies</div>
    <h2 class="section-title">Service<br>Matrix</h2>
    <p>Our services are modular and scalable. Whether you need a single remote paralegal or a full system overhaul, we deploy precisely what is required.</p>
    <div class="stats">
      <div class="stat"><b>24h</b><span>REMOTE SUPPORT</span></div>
      <div class="stat"><b>12+</b><span>COUNTRIES</span></div>
    </div>
  </div>
  <div class="service-list">
    <div class="service"><div class="service-name"><h3>Paralegal Services</h3><em>Remote &amp; In-Office Placement</em></div><p>Scalable staffing solutions. We provide vetted paralegals for document review, filing, and case management on a per-project or permanent basis.</p></div>
    <div class="service"><div class="service-name"><h3>System Implementation</h3><em>Workflow &amp; Training</em></div><p>Complete overhaul of practice management software. We handle the migration, configuration, and staff training to ensure operational efficiency.</p></div>
    <div class="service"><div class="service-name"><h3>Probate &amp; Assets</h3><em>Heir Finder &amp; Location</em></div><p>Advanced investigative services for probate law. We locate missing heirs and identify hidden global assets to close estates faster.</p></div>
    <div class="service"><div class="service-name"><h3>Logistics</h3><em>Service by Mail &amp; Ex-Parte</em></div><p>Reliable process service by mail and handling of time-sensitive Ex-Parte notices. We ensure your procedural requirements are met perfectly.</p></div>
  </div>
</section>

<section class="research">
  <div class="research-head">
    <div class="eyebrow">Advanced Analytics</div>
    <h2 class="section-title">Research<br>Division</h2>
    <p class="research-quote">"Litigation is information warfare. We provide the ammunition."</p>
  </div>
  <div class="cards">
    <article class="card">
      <svg width="18" height="20" viewBox="0 0 18 20" fill="none" stroke="#b5541c" stroke-width="1.3"><path d="M2 1h9l5 5v13H2z"/><path d="M11 1v5h5"/><circle cx="8.5" cy="12" r="2.5"/><path d="M10.4 13.9l2 2"/></svg>
      <span class="tag">DATA PRODUCT</span>
      <h4>Judge Motion Ruling History</h4>
      <p>We compile and analyze specific judges' historical rulings on motions similar to yours. Understand their tendencies, preferences, and citation patterns before you draft your first argument.</p>
      <ul><li>Win/Loss Probability Analysis</li><li>Citation Frequency Metrics</li></ul>
    </article>
    <article class="card">
      <svg width="20" height="20" viewBox="0 0 20 20" fill="none" stroke="#b5541c" stroke-width="1.3"><circle cx="10" cy="10" r="8.5"/><path d="M10 1.5v4M10 14.5v4M1.5 10h4M14.5 10h4"/></svg>
      <span class="tag">DATA PRODUCT</span>
      <h4>Opposition Research</h4>
      <p>Deep dive into opposing counsel's historical filings. We identify patterns in their delay tactics, settlement thresholds, and argumentation styles across multiple jurisdictions.</p>
      <ul><li>Procedural Habit Identification</li><li>Settlement History Review</li></ul>
    </article>
  </div>
</section>

<section class="contact">
  <h2 class="contact-title">Start a Case File</h2>
  <div class="form">
    <div class="row"><div class="field">NAME</div><div class="field">EMAIL</div></div>
    <div class="field select"><span>Select Area of Interest</span>
      <svg width="8" height="5" viewBox="0 0 8 5"><path d="M1 1l3 3 3-3" fill="none" stroke="#555"/></svg></div>
    <div class="field details">DETAILS</div>
    <div class="submit">SUBMIT REQUEST
      <svg width="7" height="7" viewBox="0 0 7 7"><path d="M1 6l5-5M2 1h4v4" fill="none" stroke="#fff" stroke-width="1"/></svg></div>
  </div>
  <p class="legal">Velmora Brightstead Ltd.<br>New York • London • Singapore</p>
</section>
</body>
</html>
```